Youth Sports Banner Ad - 3x5 ft banner special!

We are looking for a full page ad (8.5x11") to advertise our banner services for Youth Sports leagues. The flyers will be handed out to teams and parents in hopes to draw their business to us for team banners.
We want to show our logo, address (4187 Verbena Ln. Paso Robles). Please include that we are offering a youth sports special price on 3x5 ft team banners for $115 (plus tax). The pricing will include 1 layout with up to 2 revisions. We would like the ad to grab the attention of the audience and ask them to "Call, Email or Stop in Today!"

Our info that needs to be on the banner includes:
email: info@markwell47.net
phone: 805-291-6583

We want to really focus on our quick turnaround as we will be producing the banners withing 1-2 business days after artwork approval.
We would like to include the banner samples if possible, and if you see fit, also include that we would like the potential customer to email us their teams name, roster, and colors to help speed up the layout process.

Target Market(s)

Parents of kids playing youth sports. The flyer is meant to increase awareness of our sign shop, while offering a great discount on banners for youth sports banners.

Font styles to use
Sans Serif

Colors

Designer to choose colors to be used in the design.

Requirements
Must have
• Our logo, $115 plus tax banner price, our business information, request to send over all team information including name, roster, and team colors.
Nice to have
• Would like to see color in the ad! If you can tie in the Kelly green from our logo, that would be great.

```html
<!DOCTYPE html>
<html lang="en">
<head>
<meta charset="utf-8">
<title>Markwell Signs – Youth Sports Banner Special</title>
<link rel="stylesheet" href="https://fonts.googleapis.com/css2?family=Oswald:wght@500;700&family=Roboto+Condensed:wght@400;700&family=Open+Sans:wght@600;700&display=swap">
<style>
:root{
  --page:#e4e4e4;
  --green:#5cb83a;
  --green-dark:#3f9a2a;
  --pink:#e5166f;
  --purple:#7b3f98;
  --purple-dark:#4a1f63;
  --yellow:#fff200;
  --ink:#1d1d1d;
  --white:#ffffff;
}
*{box-sizing:border-box;margin:0;padding:0}
html,body{width:707px;height:1200px;overflow:hidden;background:var(--page)}
.flyer{position:absolute;left:0;top:141px;width:707px;height:918px;overflow:hidden;
  background:radial-gradient(ellipse at 50% 40%,var(--green) 0%,var(--green-dark) 100%);
  font-family:"Roboto Condensed",sans-serif;color:var(--white)}
.shapes{position:absolute;inset:0}
.abs{position:absolute}
.brand{left:0;width:707px;top:62px;text-align:center;font-family:"Oswald",sans-serif;font-weight:700;
  font-size:56px;line-height:60px;letter-spacing:1px;color:var(--white)}
.offer-band{left:99px;top:255px;width:403px;height:68px;background:var(--pink);
  font-family:"Oswald",sans-serif;font-weight:700;font-size:44px;line-height:68px;padding-left:22px}
.headline{left:150px;top:336px;font-family:"Oswald",sans-serif;font-weight:700;font-size:60px;line-height:64px;
  color:var(--white);text-shadow:3px 3px 0 var(--purple-dark);letter-spacing:1px}
.price-line{left:150px;top:400px;font-family:"Oswald",sans-serif;font-weight:700;font-size:46px;line-height:52px;color:var(--yellow);letter-spacing:1px}
.size-tag{left:136px;top:455px;width:121px;height:34px;background:var(--green);font-size:27px;line-height:34px;text-align:center;font-weight:400}
.banner-word{left:270px;top:455px;font-size:31px;line-height:34px;font-weight:400;letter-spacing:.5px}
.terms{left:119px;top:494px;width:226px;height:60px;background:var(--yellow);color:var(--ink);
  font-family:"Open Sans",sans-serif;font-weight:600;font-size:9.5px;line-height:15px;padding:7px 0 0 14px;list-style:none}
.terms li::before{content:"• "}
.price-tag{left:352px;top:488px;width:166px;height:74px;background:var(--yellow);color:var(--ink);
  transform:rotate(-2deg);text-align:center;padding-top:6px}
.price-main{font-family:"Oswald",sans-serif;font-weight:500;font-size:36px;line-height:44px}
.price-note{font-family:"Roboto Condensed",sans-serif;font-weight:700;font-size:13px;line-height:16px;letter-spacing:1px}
.cta{left:459px;top:552px;width:164px;height:164px;border-radius:50%;background:var(--pink);
  border:3px dotted var(--white);outline:6px solid var(--pink);text-align:center;padding-top:44px}
.cta-ask{font-family:"Roboto Condensed",sans-serif;font-weight:700;font-size:18px;line-height:21px}
.cta-now{font-family:"Oswald",sans-serif;font-weight:700;font-size:30px;line-height:36px;color:var(--yellow)}
.prints-title{left:70px;width:370px;top:664px;text-align:center;font-size:16px;color:var(--purple-dark);font-weight:700}
.prints-title::after{content:"";display:block;width:140px;height:1px;background:var(--purple-dark);margin:2px auto 0}
.sample{top:697px;width:181px;height:104px;border:3px solid var(--white)}
.sample-blue{left:70px;background:linear-gradient(135deg,#1c2b6b,#3a4aa8)}
.sample-orange{left:260px;background:linear-gradient(135deg,#111,#3a2a12 60%,#f08a1c)}
.social{top:852px;width:26px;height:26px;border-radius:50%;background:var(--purple-dark)}
.address{left:328px;top:858px;font-family:"Open Sans",sans-serif;font-weight:700;font-size:14px;line-height:18px}
.contact{left:465px;top:818px;font-family:"Open Sans",sans-serif}
.contact-row{display:flex;align-items:center;gap:8px;font-weight:600;font-size:15px;line-height:28px}
.contact-row.phone{font-family:"Oswald",sans-serif;font-weight:500;font-size:29px;line-height:38px}
.contact svg{flex:none}
.divider{left:453px;top:825px;width:2px;height:80px;background:var(--white)}
</style>
</head>
<body>
<main class="flyer">
  <svg class="shapes" width="707" height="918" viewBox="0 0 707 918" aria-hidden="true">
    <polygon points="119,300 530,300 603,300 560,420 603,542 119,542" fill="var(--purple)"/>
    <polygon points="119,552 330,552 363,660" fill="var(--purple-dark)"/>
    <line x1="541" y1="520" x2="541" y2="552" stroke="var(--white)" stroke-width="2"/>
    <circle cx="541" cy="518" r="4" fill="none" stroke="var(--white)" stroke-width="2"/>
    <polygon points="0,799 330,918 0,918" fill="var(--pink)"/>
    <polygon points="707,759 707,918 218,918" fill="var(--purple-dark)"/>
  </svg>

  <div class="abs brand">MARKWELL<br>SIGNS</div>

  <div class="abs offer-band">WE ARE OFFERING</div>
  <div class="abs headline">YOUTH SPORTS</div>
  <div class="abs price-line">SPECIAL PRICE</div>
  <div class="abs size-tag">ON 3x5 ft</div>
  <div class="abs banner-word">TEAM BANNERS</div>
  <ul class="abs terms">
    <li>1-2 Business Days After Artwork Approval</li>
    <li>1 Layout with up to 2 revisions.</li>
    <li>Email us your team name, roster &amp; colors!</li>
  </ul>
  <div class="abs price-tag">
    <div class="price-main">FOR $115</div>
    <div class="price-note">PLUS TAX</div>
  </div>

  <div class="abs cta">
    <div class="cta-ask">CALL,<br>EMAIL OR STOP</div>
    <div class="cta-now">IN TODAY!</div>
  </div>

  <div class="abs prints-title">Our Recent Prints</div>
  <div class="abs sample sample-blue" role="img" aria-label="Sample team banner in navy with a team mascot and player roster"></div>
  <div class="abs sample sample-orange" role="img" aria-label="Sample team banner in black and orange with a team mascot and player roster"></div>

  <div class="abs social" style="left:27px"></div>
  <div class="abs social" style="left:62px"></div>

  <svg class="abs" style="left:309px;top:862px" width="14" height="18" viewBox="0 0 14 18" aria-hidden="true">
    <path d="M7 1a6 6 0 0 1 6 6c0 4-6 10-6 10S1 11 1 7a6 6 0 0 1 6-6z" fill="none" stroke="var(--white)" stroke-width="1.6"/>
    <circle cx="7" cy="7" r="2" fill="var(--white)"/>
  </svg>
  <div class="abs address">4187 Verbena Ln.<br>Paso Robles</div>

  <div class="abs divider"></div>
  <div class="abs contact">
    <div class="contact-row phone">
      <svg width="20" height="20" viewBox="0 0 20 20" aria-hidden="true"><circle cx="10" cy="10" r="9" fill="none" stroke="var(--white)" stroke-width="1.6"/><path d="M7 5l2 3-1 1c1 2 2 3 3 3l1-1 3 2-1 2c-4 0-8-4-8-8z" fill="var(--white)"/></svg>
      805-291-6583
    </div>
    <div class="contact-row">
      <svg width="16" height="16" viewBox="0 0 16 16" aria-hidden="true"><circle cx="8" cy="8" r="7.5" fill="var(--white)"/><rect x="4" y="5" width="8" height="6" fill="none" stroke="var(--purple-dark)" stroke-width="1.2"/><path d="M4 5l4 3 4-3" fill="none" stroke="var(--purple-dark)" stroke-width="1.2"/></svg>
      info@markwell47.net
    </div>
    <div class="contact-row">
      <svg width="16" height="16" viewBox="0 0 16 16" aria-hidden="true"><circle cx="8" cy="8" r="7.5" fill="var(--white)"/><circle cx="8" cy="8" r="4" fill="none" stroke="var(--purple-dark)" stroke-width="1.2"/><path d="M4 8h8M8 4v8" stroke="var(--purple-dark)" stroke-width="1"/></svg>
      www.markwell47.net
    </div>
  </div>
</main>
</body>
</html>
```